Food Packaging Design Project

We already have an established brand but feel that our packaging could be stronger. We would like the same logo outline , colour scheme and wording on the front and back... so that it is still recognisable to our customers but just a little more professional looking with the wow factor to help it stand out on the shelve.

We need both front and back design with colours on the back also.

The design must contain our registered logo design but can be added to.

The back doesn't have to be split into 2 columns as in the image provided.

The packets arn't the same as the old packs (as in picture attached) but instead will be pouches with solid edges.

We will need working files so that we can amend ourselves once the final design has been chosen.

Thanks in advance!
Updates

Project Deadline Extended
Reason: havent quite got what we are after, not enough designs submitted.

Requirements
Must have
• The design must contain our registered logo... see image attached.

Must contain our colour that we currently have.

Must have the same writing on the front and back.

```html
<!DOCTYPE html>
<html lang="en">
<head>
<meta charset="utf-8">
<title>Slim Strands – Gluten Free Pouch</title>
<link rel="stylesheet" href="https://fonts.googleapis.com/css2?family=Open+Sans:ital,wght@0,400;0,600;0,700;1,700&display=swap">
<style>
  :root {
    --stage: #efefef;
    --green: #7cb84a;
    --green-dark: #5b8e36;
    --green-deep: #4f7f2e;
    --band-light: #d9615b;
    --band-dark: #9f3a42;
    --cream: #fdf9dc;
    --cream-deep: #fbf1a6;
    --yellow: #f7e36a;
    --white: #ffffff;
    --tape-text: #6a4418;
  }
  * { margin: 0; padding: 0; box-sizing: border-box; }
  html, body {
    width: 1000px; height: 1200px; overflow: hidden;
    background: var(--stage);
    font-family: "Open Sans", Arial, sans-serif;
  }
  .canvas { position: relative; width: 1000px; height: 1200px; }

  .pouch {
    position: absolute; left: 120px; top: 90px;
    width: 760px; height: 1020px;
    border-radius: 14px; overflow: hidden;
    background: linear-gradient(180deg, var(--cream) 0%, var(--cream-deep) 100%);
    box-shadow: 0 6px 18px rgba(0,0,0,.18);
  }
  .pouch-shapes { position: absolute; inset: 0; }

  .brand-name {
    position: absolute; left: 90px; top: 160px;
    color: var(--white); font-weight: 700; line-height: 1;
  }
  .brand-name .line-1 { display: block; font-size: 74px; margin-left: 125px; }
  .brand-name .line-2 { display: block; font-size: 128px; letter-spacing: -2px; margin-top: 6px; }

  .band-label {
    position: absolute; left: 425px; top: 478px;
    font-size: 38px; font-weight: 600; letter-spacing: 5px; line-height: 1;
    color: var(--cream); white-space: nowrap;
    transform: translate(-50%, -50%) rotate(-9deg);
  }

  .figure-art {
    position: absolute; left: 130px; top: 530px;
    width: 300px; height: 400px; border-radius: 40% 40% 30% 30%;
    background: radial-gradient(ellipse at 50% 40%, #d6eaa0 0%, #eef5c2 55%, rgba(253,249,220,0) 80%);
  }

  .tagline {
    position: absolute; left: 45px; top: 862px;
    font-size: 15px; font-weight: 700; font-style: italic; line-height: 1;
    color: var(--tape-text);
    transform: rotate(13deg); transform-origin: left center;
    white-space: nowrap;
  }

  .organic-mark {
    position: absolute; left: 490px; top: 575px;
    width: 70px; height: 70px; border-radius: 8px;
    background: linear-gradient(135deg, var(--green) 0%, var(--green-dark) 100%);
  }
  .organic-label {
    position: absolute; left: 545px; top: 648px;
    font-size: 32px; color: var(--green-dark); line-height: 1;
  }

  .claims { position: absolute; left: 392px; top: 870px; display: flex; gap: 11px; }
  .claim {
    width: 72px; height: 108px; position: relative;
    background: var(--green-dark); border-radius: 14px 14px 6px 6px;
    text-align: center; color: var(--white);
    padding-top: 10px;
  }
  .claim-level { display: block; font-size: 20px; font-weight: 700; color: var(--yellow); line-height: 1.05; }
  .claim-item { display: block; font-size: 16px; line-height: 1.2; }
  .claim-value {
    position: absolute; left: 5px; bottom: 6px; width: 62px; height: 32px;
    border-radius: 50%; background: var(--yellow);
    color: var(--green-deep); font-size: 18px; font-weight: 700; line-height: 32px;
  }
</style>
</head>
<body>
<div class="canvas">
  <div class="pouch">
    <svg class="pouch-shapes" width="760" height="1020" viewBox="0 0 760 1020" aria-hidden="true">
      <defs>
        <linearGradient id="bandFill" x1="0" y1="0" x2="1" y2="0">
          <stop offset="0" stop-color="#9f3a42"/>
          <stop offset="0.5" stop-color="#d9615b"/>
          <stop offset="1" stop-color="#9f3a42"/>
        </linearGradient>
      </defs>
      <path d="M0,0 H760 V405 Q380,440 0,540 Z" fill="#7cb84a"/>
      <path d="M0,540 Q380,440 760,405 V462 Q380,500 0,600 Z" fill="url(#bandFill)"/>
    </svg>

    <div class="brand-name"><span class="line-1">Slim</span><span class="line-2">Strands</span></div>

    <div class="band-label">Gluten Free</div>

    <div class="figure-art" role="img" aria-label="Illustration of a slender dancing figure wrapped in a tape measure"></div>
    <div class="tagline">The Alternatives to Pasta for Weight Loss</div>

    <div class="organic-mark" role="img" aria-label="Green leaf icon"></div>
    <span class="organic-label">Organic</span>

    <div class="claims">
      <div class="claim"><span class="claim-level">Zero</span><span class="claim-item">Fat</span><span class="claim-value">0%</span></div>
      <div class="claim"><span class="claim-level">Zero</span><span class="claim-item">Sugar</span><span class="claim-value">0%</span></div>
      <div class="claim"><span class="claim-level">Low</span><span class="claim-item">Calorie</span><span class="claim-value">0%</span></div>
      <div class="claim"><span class="claim-level">Low</span><span class="claim-item">Carb</span><span class="claim-value">0%</span></div>
    </div>
  </div>
</div>
</body>
</html>
```